Movie Poster - Beneath The Amber Tide

Documentary-film poster design.
Attached is a PDF brief with information on what is required and examples of poster designs I like.

The project is a true crime / mystery documentary film. Set in the Soviet Union in 1959.

Colors
3276b5
85abd2
ec1f27

```html
<!DOCTYPE html>
<html lang="en">
<head>
<meta charset="utf-8">
<title>Beneath The Amber Tide — Poster</title>
<link rel="stylesheet" href="https://fonts.googleapis.com/css2?family=Anton&family=Bebas+Neue&family=Open+Sans:wght@600&family=Oxygen:wght@700&display=swap">
<style>
  :root {
    --deep-blue: #2b5683;
    --mid-blue: #3276b5;
    --pale-blue: #85abd2;
    --snow: #f4f6f8;
    --title-ice: #dfe7f0;
    --signal-red: #a8141b;
    --credit-ink: #1f3f66;
  }
  * { margin: 0; padding: 0; box-sizing: border-box; }
  html, body { width: 810px; height: 1200px; overflow: hidden; }
  body { position: relative; background: var(--snow); }

  .poster-scene {
    position: absolute; inset: 0;
    background:
      radial-gradient(ellipse 420px 300px at 300px 640px, rgba(255,255,255,0.55), rgba(255,255,255,0) 70%),
      linear-gradient(180deg, #2a5280 0%, #3b6792 22%, #7f9cbb 45%, #c3d1df 62%, #eef2f6 78%, var(--snow) 100%);
  }

  .tagline {
    position: absolute; top: 40px; left: 200px; width: 360px;
    text-align: center;
    font-family: "Oxygen", sans-serif; font-weight: 700;
    font-size: 19px; line-height: 23px; color: #ffffff;
    white-space: nowrap;
  }

  .film-title {
    position: absolute; top: 150px; right: 18px;
    text-align: right;
    font-family: "Anton", sans-serif; font-weight: 400;
    font-size: 150px; line-height: 156px;
    color: var(--title-ice);
    text-transform: uppercase;
    letter-spacing: 1px;
    white-space: nowrap;
  }
  .film-title span { display: block; }

  .subtitle {
    position: absolute; top: 926px; left: 0; width: 810px;
    text-align: center;
    font-family: "Open Sans", sans-serif; font-weight: 600;
    font-size: 25px; color: var(--signal-red);
  }

  .credits {
    position: absolute; top: 1018px; left: 15px; width: 780px;
    font-family: "Bebas Neue", sans-serif;
    color: var(--credit-ink);
  }
  .credit-row {
    display: flex; justify-content: center; align-items: center;
    height: 32px; gap: 7px;
    white-space: nowrap;
  }
  .credit { display: flex; align-items: center; gap: 3px; flex: none; }
  .credit-role {
    font-size: 10px; line-height: 10px; text-align: right;
  }
  .credit-name { font-size: 26px; line-height: 28px; }
</style>
</head>
<body>
  <div class="poster-scene" role="img" aria-label="Photograph of a line of skiers with backpacks and poles trudging through a blue, snowy blizzard"></div>

  <p class="tagline">Nine Dead Hikers<br>Sixty Years Of Secrets<br>Russia's Greatest Mystery Uncovered</p>

  <h1 class="film-title"><span>Beneath</span><span>The Amber</span><span>Tide</span></h1>

  <p class="subtitle">The true story of the Kholvor Ridge Incident</p>

  <div class="credits">
    <div class="credit-row">
      <div class="credit"><span class="credit-role">Edited<br>by</span><span class="credit-name">Lorem Ipsum</span></div>
      <div class="credit"><span class="credit-role">Art<br>director</span><span class="credit-name">Lorem Ipsum</span></div>
      <div class="credit"><span class="credit-role">Edited<br>by</span><span class="credit-name">Lorem Ipsum</span></div>
      <div class="credit"><span class="credit-role">Creatures<br>designed by</span><span class="credit-name">Lorem Ipsum</span></div>
      <div class="credit"><span class="credit-role">3D visual<br>effects by</span><span class="credit-name">Lorem Ipsum</span></div>
    </div>
    <div class="credit-row">
      <div class="credit"><span class="credit-role">Written<br>by</span><span class="credit-name">Lorem Ipsum</span></div>
      <div class="credit"><span class="credit-role">Production<br>designer</span><span class="credit-name">Lorem Ipsum</span></div>
      <div class="credit"><span class="credit-role">Director of<br>photography</span><span class="credit-name">Lorem Ipsum</span></div>
      <div class="credit"><span class="credit-role">Line<br>producer</span><span class="credit-name">Lorem Ipsum</span></div>
      <div class="credit"><span class="credit-role">Music<br>by</span><span class="credit-name">Lorem Ipsum</span></div>
    </div>
    <div class="credit-row">
      <div class="credit"><span class="credit-role">Story<br>by</span><span class="credit-name">Lorem Ipsum</span></div>
      <div class="credit"><span class="credit-role">Based on the<br>novel by</span><span class="credit-name">Lorem Ipsum</span></div>
      <div class="credit"><span class="credit-role">Story<br>by</span><span class="credit-name">Lorem Ipsum</span></div>
      <div class="credit"><span class="credit-role">Based on the<br>novel by</span><span class="credit-name">Lorem Ipsum</span></div>
      <div class="credit"><span class="credit-role">Special<br>effects by</span><span class="credit-name">Lorem Ipsum</span></div>
    </div>
    <div class="credit-row">
      <div class="credit"><span class="credit-role">Story<br>by</span><span class="credit-name">Lorem Ipsum</span></div>
      <div class="credit"><span class="credit-role">Based on the<br>novel by</span><span class="credit-name">Lorem Ipsum</span></div>
    </div>
  </div>
</body>
</html>
```